Halvorn Analytics, Inc. Site Design Project

Halvorn Analytics, Inc is my private and small research office.
This naming shows:
We investigate every(*: asterisk) issue to support society.
We investigate "a star risk" which means every critical things for example, information security, branding, public communication - to understand for our clients - especially innovative person.
Last year, we had faced the great disaster in Japan, we investigated the damaged place, schools, and local governments, and supported communities like PLUMvaskel.
So I want to get a high concept sites with good logo and to use card, website, and our letter.
Reason: We would like to look for more competitive candidates.
I uploaded the latest logo. If you have any idea to adapt it to your design, I appreciate it.
Target Market(s)
* marketing section of leading companies(enterprises)
* promotion agencies of government
* futurist and researcher
* business managers
Industry/Entity Type
Communication
Logo Text
for desirable future
Look and feel
Each slider illustrates characteristics of the customer's brand and the style your logo design should communicate.

```html
<!DOCTYPE html>
<html lang="en">
<head>
<meta charset="utf-8">
<title>Halvorn Analytics — Research</title>
<link rel="stylesheet" href="https://fonts.googleapis.com/css2?family=Arimo:ital,wght@0,400;0,700;1,700&family=Baumans&display=swap">
<style>
  :root {
    --page: #222224;
    --ink: #ffffff;
    --muted: #d8d8d8;
    --rule: #6b6b6b;
    --gallery-bg: #857a76;
    --gallery-line: #d0d0d0;
    --caption-red: #e0202a;
  }
  * { box-sizing: border-box; margin: 0; padding: 0; }
  html, body { width: 1200px; height: 1170px; overflow: hidden; background: var(--page); }
  body { position: relative; font-family: "Arimo", Arial, sans-serif; color: var(--ink); }

  .brand { position: absolute; left: 31px; top: 18px; }
  .brand-name { font-family: "Arimo", Arial, sans-serif; font-weight: 700; font-size: 56px; line-height: 60px; letter-spacing: 1px; color: var(--ink); }
  .brand-sub { font-family: "Arimo", Arial, sans-serif; font-weight: 700; font-size: 13px; letter-spacing: 8px; color: var(--ink); margin-top: 2px; }

  .tagline { position: absolute; right: 25px; top: 10px; font-family: "Baumans", sans-serif; font-size: 22px; color: var(--ink); white-space: nowrap; }

  .main-nav { position: absolute; top: 73px; left: 0; width: 1200px; height: 20px; }
  .main-nav a { position: absolute; font-family: "Baumans", sans-serif; font-size: 15px; color: var(--ink); text-decoration: none; letter-spacing: .5px; white-space: nowrap; }

  .hero { position: absolute; left: 30px; top: 107px; width: 1141px; height: 452px; display: flex; gap: 2px; background: #3a3a3a; }
  .hero-panel { position: relative; flex: 1; }
  .hero-panel.lab { background: linear-gradient(135deg, #2a8a8a, #7a9aa0 45%, #3d5a66); }
  .hero-panel.dishes { background: linear-gradient(180deg, #1f5fc8, #9fc1ea 40%, #e6e6ea 65%, #b08070); }
  .hero-panel.microscope { background: linear-gradient(120deg, #2d2f33, #7c7f86 45%, #e6e2e0 75%, #c9b6a8); }
  .hero-caption { position: absolute; left: 0; right: 0; bottom: 10px; text-align: center; font-family: "Arimo", Arial, sans-serif; font-style: italic; font-weight: 700; font-size: 20px; letter-spacing: 1.5px; color: var(--caption-red); text-shadow: -1px -1px 0 #fff, 1px -1px 0 #fff, -1px 1px 0 #fff, 1px 1px 0 #fff; }

  .intro { position: absolute; top: 572px; left: 30px; width: 1141px; height: 212px; }
  .intro-col { position: absolute; top: 0; height: 212px; }
  .intro-col + .intro-col { border-left: 1px solid var(--rule); }
  .intro-col h2 { font-size: 17px; font-weight: 700; margin-top: 15px; margin-bottom: 8px; }
  .intro-col h2.vision { font-family: "Baumans", sans-serif; font-weight: 400; font-size: 20px; margin-top: 10px; }
  .intro-col p { font-size: 14.5px; line-height: 18px; color: var(--muted); width: 355px; }
  .read-more { position: absolute; bottom: 6px; right: 24px; font-size: 17px; font-weight: 700; color: var(--ink); text-decoration: none; white-space: nowrap; }

  .gallery-title { position: absolute; left: 48px; top: 834px; font-size: 22px; font-weight: 700; }
  .gallery-rule { position: absolute; left: 45px; top: 875px; width: 524px; height: 2px; background: var(--rule); }
  .gallery { position: absolute; left: 44px; top: 896px; width: 1113px; height: 221px; background: var(--gallery-bg); border: 1px solid var(--gallery-line); }
  .thumb { position: absolute; top: 14px; height: 194px; border: 3px solid #fff; border-radius: 3px; }
  .thumb.flowers { left: 18px; width: 246px; background: linear-gradient(180deg, #3a86e0, #a8d0f4 55%, #4caa2a 75%, #2f8a1c); }
  .thumb.relief { left: 285px; width: 256px; background: linear-gradient(160deg, #4f7a3c, #9a9088 50%, #6f6a5a); }
  .thumb.satellite { left: 563px; width: 256px; background: linear-gradient(170deg, #0a0e1c, #3a5ca8 55%, #c4d4ea); }
  .thumb.stream { left: 840px; width: 252px; background: linear-gradient(180deg, #6d8a56, #9aa28e 50%, #4f8a36); }

  .copyright { position: absolute; left: 44px; top: 1137px; font-size: 14.5px; color: var(--muted); }
</style>
</head>
<body>
  <header>
    <div class="brand">
      <div class="brand-name">HALVORN</div>
      <div class="brand-sub">ANALYTICS</div>
    </div>
    <p class="tagline">We investigate every critical issue to support society</p>
    <nav class="main-nav">
      <a href="#" style="left:609px">HOME</a>
      <a href="#" style="left:682px">ABOUT US</a>
      <a href="#" style="left:785px">SERVICES</a>
      <a href="#" style="left:886px">PRODUCTS</a>
      <a href="#" style="left:994px">ENQUIRY</a>
      <a href="#" style="left:1087px">CONTACT US</a>
    </nav>
  </header>

  <section class="hero">
    <div class="hero-panel lab" role="img" aria-label="Two researchers in safety glasses working inside a lab instrument">
      <span class="hero-caption">RESOURCES.</span>
    </div>
    <div class="hero-panel dishes" role="img" aria-label="Satellite dishes under a blue sky with clouds">
      <span class="hero-caption">EQUIPMENT.</span>
    </div>
    <div class="hero-panel microscope" role="img" aria-label="Researcher in a lab coat looking into a microscope">
      <span class="hero-caption">UTILITIES.</span>
    </div>
  </section>

  <section class="intro">
    <div class="intro-col" style="left:0; width:378px; padding-left:16px;">
      <h2>Resources...............</h2>
      <p>Lorem ipsum dolor sit amet, consectetur adipiscing elit. Sed tristique facilisis ipsum eget tempus. Vestibulum et consectetur sem. Aliquam condimentum, justo ut egestas elementum, nisl dolor tincidunt mi, lacinia gravida ligula lectus et est. Class aptent taciti sociosqu ad litora torquent per conubia nostra, per inceptos himenaeos</p>
      <a class="read-more" href="#">Read More.......</a>
    </div>
    <div class="intro-col" style="left:378px; width:378px; padding-left:18px;">
      <h2 class="vision">OUR VISION</h2>
      <p>Lorem ipsum dolor sit amet, consectetur adipiscing elit. Sed tristique facilisis ipsum eget tempus. Vestibulum et consectetur sem. Aliquam condimentum, justo ut egestas elementum, nisl dolor tincidunt mi, lacinia gravida ligula lectus et est. Class aptent taciti sociosqu ad litora torquent per conubia nostra, per inceptos himenaeos</p>
      <a class="read-more" href="#">Read More.......</a>
    </div>
    <div class="intro-col" style="left:756px; width:385px; padding-left:22px;">
      <h2>Latest News...............</h2>
      <p>Lorem ipsum dolor sit amet, consectetur adipiscing elit. Sed tristique facilisis ipsum eget tempus. Vestibulum et consectetur sem. Aliquam condimentum, justo ut egestas elementum, nisl dolor tincidunt mi, lacinia gravida ligula lectus et est. Class aptent taciti sociosqu ad litora torquent per conubia nostra, per inceptos himenaeos</p>
      <a class="read-more" href="#">Read More........</a>
    </div>
  </section>

  <section>
    <h2 class="gallery-title">IMAGE GALLERY</h2>
    <div class="gallery-rule"></div>
    <div class="gallery">
      <div class="thumb flowers" role="img" aria-label="Tulips on green grass under a sunny sky"></div>
      <div class="thumb relief" role="img" aria-label="Relief workers walking through a damaged town"></div>
      <div class="thumb satellite" role="img" aria-label="Satellite orbiting above the Earth"></div>
      <div class="thumb stream" role="img" aria-label="Stream running through green overgrown ground"></div>
    </div>
  </section>

  <footer class="copyright">Copyright 2012.All rights reserved.</footer>
</body>
</html>
```